job report

Designer – Professional Plumbing Job Report Template

Overview

We are seeking a skilled designer to create a professional, easy-to-use Job Report template for a commercial and maintenance plumbing business.
The report will be used for clients, property managers, facilities managers, strata, and retail centres and must clearly communicate findings, works completed, and recommendations in a polished, compliant, and branded format.

The final document must be suitable for PDF delivery, email, and ongoing reuse.

Objectives

Present plumbing works in a clear, professional, and defensible report format

Improve client understanding of findings and recommendations

Provide a repeatable template that can be used across maintenance, reactive, and investigative works

Allow easy insertion of text, tables, and photos

Report Structure (Minimum Inclusions)
1. Cover Page

Company logo and branding

Report title (e.g. Plumbing Job Report / Investigation Report)

Client name

Site address

Job reference / work order number

Date of attendance

Technician / contractor name

2. Client & Site Details

Client / company name

Site address

Contact person

Contact details

Access notes (after-hours, tenant access, etc.)

3. Reason for Attendance

Clear description of why attendance was required

Call-out type (reactive, scheduled maintenance, investigation, emergency, etc.)

Reported issue or scope requested by client

4. Findings / Observations

Detailed findings discovered on site

Condition of pipework, fixtures, drainage, or systems

Any contributing factors identified

Notes on compliance, wear, damage, or risk

(This section should support bullet points and paragraphs.)

5. Works Carried Out

Step-by-step description of works completed

Equipment used (e.g. jetter, CCTV camera, leak detection, flex shaft, etc.)

Repairs, replacements, testing, and verification

Confirmation that systems were tested and operational on completion

6. Photos & Visual Evidence

Clearly labelled photo sections

Before / during / after photos

Space for photo captions and explanations

Logical layout that aligns photos with written findings

7. Recommendations

Clearly separated from works completed

Urgent vs non-urgent recommendations

Preventative maintenance advice

Upgrade or replacement suggestions

Risk-based language where appropriate

8. Limitations & Exclusions

Areas not inspected

Access limitations

Assumptions made during inspection

Items outside scope of works

9. Conclusion

Summary of outcome

Confirmation of current system status

Next steps (if any)

10. Sign-Off

Contractor / technician name

Company name

Date

Optional client acknowledgement section

Design Requirements

Clean, professional layout

Commercial / trade-appropriate styling (not overly creative)

Easy-to-read fonts

Consistent headings and spacing

Logical flow for busy property managers

Editable format (Word / Google Docs / InDesign source file)

Final export-ready PDF version

Bonus (Nice to Have)

Traffic-light system (Green / Amber / Red) for condition reporting

Iconography for findings, repairs, and recommendations

Optional sections for compliance notes (AS/NCC references)

Space for QR codes or job reference numbers

Deliverables

Editable master report template

PDF version

Instructions or notes for ongoing use

```html
<!DOCTYPE html>
<html lang="en">
<head>
<meta charset="utf-8">
<title>Plumbing Job Report Template</title>
<link href="https://fonts.googleapis.com/css2?family=Poppins:ital,wght@0,400;0,500;0,600;0,700;1,400&display=swap" rel="stylesheet">
<style>
:root{
  --stage:#2b2b2b;
  --paper:#f1f1f1;
  --white:#ffffff;
  --blue:#27a9e1;
  --orange:#f3b02c;
  --ink:#222222;
  --line:#9a9a9a;
  --photo-a:#b9b4ad;
  --photo-b:#6d7f98;
}
*{margin:0;padding:0;box-sizing:border-box}
html,body{width:1200px;height:382px;overflow:hidden;background:var(--stage);font-family:'Poppins',sans-serif;color:var(--ink)}
.page{position:absolute;top:11px;width:278px;height:359px;background:var(--paper);overflow:hidden}
.page svg.art{position:absolute;left:0;top:0}
.abs{position:absolute}
.brand{position:absolute;font-weight:700;color:var(--blue);line-height:1;text-align:center;letter-spacing:.2px}
.brand--cover{left:180px;top:72px;font-size:13px;width:92px;line-height:1.05}
.brand--small{right:12px;width:60px;font-size:6.2px}
/* cover */
.cover-title{position:absolute;left:0;width:278px;top:240px;text-align:center;color:var(--white);font-weight:600;font-size:16px}
.cover-field{position:absolute;left:14px;right:15px;display:flex;align-items:flex-end;color:var(--white);font-weight:600;font-size:6.4px;white-space:nowrap}
.cover-field span.rule{flex:1;border-bottom:.6px solid rgba(255,255,255,.85);margin-left:2px;height:6px}
/* section heads */
.section-pill{position:absolute;left:0;height:15px;border-radius:0 8px 8px 0;background:linear-gradient(90deg,var(--blue) 55%,var(--orange));color:var(--white);font-weight:600;font-size:6.3px;display:flex;align-items:center;gap:5px;padding-left:12px}
.section-pill svg{width:7px;height:7px}
/* form */
.label{position:absolute;font-size:3.7px;color:var(--ink)}
.field{position:absolute;background:var(--white);border:.5px solid #8c8c8c}
.select{font-size:3.2px;font-style:italic;display:flex;align-items:center;justify-content:space-between;padding:0 4px}
.factors-title{position:absolute;left:12px;top:231px;font-size:3.7px;font-weight:600}
.factor-list{position:absolute;list-style:none;font-size:3.6px;font-style:italic}
.factor-list li{height:8.4px;display:flex;align-items:center;gap:3px}
.factor-list li::before{content:"";width:3px;height:1.6px;border-left:.6px solid var(--blue);border-bottom:.6px solid var(--blue);transform:rotate(-45deg) translateY(-.6px)}
.divider{position:absolute;left:0;right:0;top:280px;border-top:.5px solid #d2d2d2}
.notes-title{position:absolute;left:12px;top:287px;font-size:3.8px;font-weight:600}
.note{position:absolute;top:296px;width:52px;font-size:3.2px;line-height:1.45}
.note h4{color:var(--blue);font-size:3.8px;font-weight:600;margin-bottom:1.5px}
</style>
</head>
<body>

<!-- Cover -->
<section class="page" style="left:12px">
  <svg class="art" width="278" height="359" viewBox="0 0 278 359">
    <defs>
      <linearGradient id="coverGrad" x1="0" y1="1" x2="1" y2="0">
        <stop offset="0.3" stop-color="#27a9e1"/>
        <stop offset="0.75" stop-color="#f3b02c"/>
      </linearGradient>
      <linearGradient id="photoCover" x1="0" y1="0" x2="1" y2="1">
        <stop offset="0" stop-color="#e4e4e2"/>
        <stop offset="0.55" stop-color="#a9a29a"/>
        <stop offset="1" stop-color="#5e6a78"/>
      </linearGradient>
    </defs>
    <rect width="278" height="230" fill="url(#photoCover)" role="img" aria-label="Photo of a smiling plumber in overalls standing in a kitchen"/>
    <polygon points="0,78 60,228 278,228 278,359 0,359" fill="url(#coverGrad)" stroke="#ffffff" stroke-width="2"/>
  </svg>
  <div class="brand brand--cover">NORTHLINE<br>PLUMBING</div>
  <h1 class="cover-title">Plumbing Job Report</h1>
  <div class="cover-field" style="top:284px">Client Name:<span class="rule"></span></div>
  <div class="cover-field" style="top:298px">Site Address:<span class="rule"></span></div>
  <div class="cover-field" style="top:312px">Job Reference / Work order number:<span class="rule"></span></div>
  <div class="cover-field" style="top:325px">Date of Attendance:<span class="rule"></span></div>
  <div class="cover-field" style="top:339px">Technician / Contractor name:<span class="rule"></span></div>
</section>

<!-- Client & Site Details -->
<section class="page" style="left:300px">
  <svg class="art" width="278" height="359" viewBox="0 0 278 359">
    <defs>
      <linearGradient id="band" x1="0" y1="0" x2="1" y2="0">
        <stop offset="0.2" stop-color="#27a9e1"/>
        <stop offset="0.6" stop-color="#f3b02c"/>
      </linearGradient>
      <linearGradient id="photoA" x1="0" y1="0" x2="1" y2="1">
        <stop offset="0" stop-color="#c9c6c0"/>
        <stop offset="0.6" stop-color="#6d7f98"/>
        <stop offset="1" stop-color="#8e7a68"/>
      </linearGradient>
    </defs>
    <rect width="278" height="359" fill="#ffffff"/>
    <polygon points="0,0 278,0 278,155 62,155 0,24" fill="url(#photoA)" role="img" aria-label="Photo of a plumber shaking hands with a client in a plant room"/>
    <polygon points="0,155 278,155 278,359 0,359" fill="#f1f1f1"/>
    <polygon points="45,359 68,337 278,337 278,359" fill="url(#band)"/>
  </svg>
  <div class="section-pill" style="top:181px;width:100px">
    <svg viewBox="0 0 10 10"><circle cx="5" cy="3" r="2" fill="#fff"/><circle cx="2" cy="4" r="1.4" fill="#fff"/><circle cx="8" cy="4" r="1.4" fill="#fff"/><path d="M1.5 9a3.5 3 0 0 1 7 0z" fill="#fff"/></svg>
    Client &amp; Site Details
  </div>
  <div class="brand brand--small" style="top:183px">NORTHLINE<br>PLUMBING</div>
  <span class="label" style="left:12px;top:206px">Client / Company name</span>
  <span class="label" style="left:142px;top:206px">Site address</span>
  <div class="field" style="left:12px;top:214px;width:124px;height:14px"></div>
  <div class="field" style="left:142px;top:214px;width:124px;height:14px"></div>
  <span class="label" style="left:12px;top:232px">Contact person</span>
  <span class="label" style="left:142px;top:232px">Contact details</span>
  <div class="field" style="left:12px;top:240px;width:124px;height:13px"></div>
  <div class="field" style="left:142px;top:240px;width:124px;height:13px"></div>
  <span class="label" style="left:12px;top:257px">Access notes</span>
  <div class="field" style="left:12px;top:265px;width:254px;height:61px"></div>
</section>

<!-- Reason for Attendance -->
<section class="page" style="left:595px">
  <svg class="art" width="278" height="359" viewBox="0 0 278 359">
    <defs>
      <linearGradient id="band2" x1="0" y1="0" x2="1" y2="0">
        <stop offset="0.2" stop-color="#27a9e1"/>
        <stop offset="0.6" stop-color="#f3b02c"/>
      </linearGradient>
      <linearGradient id="photoB" x1="0" y1="0" x2="1" y2="1">
        <stop offset="0" stop-color="#e2e0da"/>
        <stop offset="0.5" stop-color="#5a6f9a"/>
        <stop offset="1" stop-color="#d8d6d2"/>
      </linearGradient>
    </defs>
    <rect width="278" height="359" fill="#ffffff"/>
    <polygon points="0,0 278,0 278,155 62,155 0,24" fill="url(#photoB)" role="img" aria-label="Photo of a plumber with a clipboard inspecting pipes under a kitchen sink"/>
    <polygon points="0,155 278,155 278,359 0,359" fill="#f1f1f1"/>
    <polygon points="45,359 68,337 278,337 278,359" fill="url(#band2)"/>
  </svg>
  <div class="section-pill" style="top:172px;width:113px">
    <svg viewBox="0 0 10 10"><path d="M2 0.5h4l2.5 2.5v6.5h-6.5z" fill="#fff"/><path d="M3.5 5h3M3.5 7h3" stroke="#27a9e1" stroke-width=".8"/></svg>
    Reason for Attendance
  </div>
  <div class="brand brand--small" style="top:175px">NORTHLINE<br>PLUMBING</div>
  <span class="label" style="left:12px;top:203px">Clear description of why attendance was required</span>
  <div class="field" style="left:12px;top:211px;width:254px;height:61px"></div>
  <span class="label" style="left:12px;top:279px">Call-out type</span>
  <span class="label" style="left:142px;top:279px">Reported issue</span>
  <div class="field select" style="left:12px;top:286px;width:124px;height:14px">Select type<span>&#8693;</span></div>
  <div class="field" style="left:142px;top:286px;width:124px;height:14px"></div>
</section>

<!-- Findings / Observations -->
<section class="page" style="left:889px">
  <svg class="art" width="278" height="359" viewBox="0 0 278 359">
    <defs>
      <linearGradient id="band3" x1="0" y1="0" x2="1" y2="0">
        <stop offset="0.2" stop-color="#27a9e1"/>
        <stop offset="0.6" stop-color="#f3b02c"/>
      </linearGradient>
      <linearGradient id="photoC" x1="0" y1="0" x2="1" y2="1">
        <stop offset="0" stop-color="#c08a7a"/>
        <stop offset="0.4" stop-color="#f0ebe4"/>
        <stop offset="1" stop-color="#4f6690"/>
      </linearGradient>
    </defs>
    <rect width="278" height="359" fill="#ffffff"/>
    <polygon points="0,0 278,0 278,155 62,155 0,24" fill="url(#photoC)" role="img" aria-label="Photo of a plumber explaining a pipe repair to a homeowner under a sink"/>
    <polygon points="0,155 278,155 278,359 0,359" fill="#f1f1f1"/>
    <polygon points="45,359 68,337 278,337 278,359" fill="url(#band3)"/>
  </svg>
  <div class="section-pill" style="top:178px;width:114px">
    <svg viewBox="0 0 10 10"><circle cx="4" cy="4" r="2.8" fill="none" stroke="#fff" stroke-width="1.3"/><path d="M6 6l3 3" stroke="#fff" stroke-width="1.5"/></svg>
    Findings / Observations
  </div>
  <div class="brand brand--small" style="top:181px">NORTHLINE<br>PLUMBING</div>
  <span class="label" style="left:12px;top:202px">Detailed findings discovered on site</span>
  <span class="label" style="left:142px;top:202px">Condition</span>
  <div class="field" style="left:12px;top:210px;width:124px;height:14px"></div>
  <div class="field select" style="left:142px;top:210px;width:124px;height:14px">Select type<span>&#8693;</span></div>
  <div class="factors-title">Any contributing factors identified</div>
  <ul class="factor-list" style="left:12px;top:237px">
    <li>Corroded joint fittings</li><li>Root intrusion</li><li>Poor pipe fall</li><li>Blocked vent stack</li>
  </ul>
  <ul class="factor-list" style="left:97px;top:237px">
    <li>Corroded joint fittings</li><li>Root intrusion</li><li>Poor pipe fall</li><li>Blocked vent stack</li>
  </ul>
  <ul class="factor-list" style="left:183px;top:237px">
    <li>Corroded joint fittings</li><li>Root intrusion</li><li>Poor pipe fall</li><li>Blocked vent stack</li>
  </ul>
  <div class="divider"></div>
  <div class="notes-title">Notes:</div>
  <div class="note" style="left:12px"><h4>Compliance</h4>Fittings meet current code, recheck each year.</div>
  <div class="note" style="left:77px"><h4>Wear</h4>Seals aged, replace at next scheduled visit.</div>
  <div class="note" style="left:143px"><h4>Damage</h4>Minor crack found at trap outlet joint.</div>
  <div class="note" style="left:208px"><h4>Risk</h4>Leak risk moderate if left untreated now.</div>
</section>

</body>
</html>
```